6x11 Postcard for Moving Company

Must have company logo and the company slogan underneath: "The Moving Company You Can Trust And Rely On!". Must have company phone number: 858-555-0142. Must have company email, website and address:
info@haul-pivot.com
www.haul-pivot.com
4127 Penwick Lane, Suite B1,
San Diego, CA 92177
Must have company licenses listed in the following format:
CAL-T# 574318 | CA# 208751 | MC# 362940 | USDOT# 7140829

Must include the following services:
Packing - Moving - Unpacking
Loading - Unloading
Storage In Transit
Long Term Storage
Local - Long Distance
Residential - Commercial
Licensed - Insured
Free Onsite and Video Estimates

And please include the following text above or below the phone number: "Call For FREE Friendly Estimates and Advice!"

Target Market(s)

New Homes that go on sale and Home that were sold and in pending status.

Industry/Entity Type

Moving Company

Colors

Designer to choose colors to be used in the design.

Requirements
Must have
• A photo of a family on the front of the postcard. Must be looking like a real photo of the actual owner of the company with wife and 2 kids (not just a basic stock family photo). Must have Qorvix Assurance Logo and the text "Qorvix Assured". Must say/include 5 star rating on Tarnly, Qorvix, Nestplanner, Chatterwall, Pinbrook. Must include FQC A+ Accreditation Logo. Must include the Certified HaulSure Logo (see attached) and the Golden Haul Expert badege. Must have a Book Online Option. Must leave space for FMDA permit for postage. Must include the following deals: $250 Off Long Distance Moves, $50 Off Local Moves, Free Boxes (*call for details), 1 Month Storage Free. (in smaller text must say: *Offers can not be combined with other offers)

```html
<!DOCTYPE html>
<html lang="en">
<head>
<meta charset="utf-8">
<title>Haul Pivot Postcard</title>
<link rel="stylesheet" href="https://fonts.googleapis.com/css2?family=Oswald:wght@500;700&family=Open+Sans:wght@600&family=Roboto:wght@400;700&display=swap">
<style>
  :root {
    --stage: #8e8e8e;
    --navy: #2e3a63;
    --red: #ec1c24;
    --white: #ffffff;
    --paper: #ffffff;
    --rule: #b9b9b9;
    --stamp: #dcdcdc;
    --photo-light: #e9edf2;
    --photo-mid: #c6a58f;
    --photo-blue: #7f9cc9;
  }
  * { margin: 0; padding: 0; box-sizing: border-box; }
  html, body { width: 1200px; height: 1100px; overflow: hidden; background: var(--stage); }
  .card {
    position: absolute; left: 120px; width: 944px; height: 515px;
    background: var(--navy); overflow: hidden;
  }
  .card--front { top: 23px; }
  .card--back { top: 561px; }
  .card__art { position: absolute; inset: 0; width: 944px; height: 515px; }

  /* Front */
  .brand { position: absolute; left: 30px; top: 60px; width: 256px; text-align: center; }
  .brand__mark { width: 70px; height: 70px; border-radius: 50%; background: var(--red); margin: 0 auto 60px; }
  .brand__name {
    font-family: "Oswald", sans-serif; font-weight: 700; font-size: 46px; line-height: 1;
    color: var(--white); letter-spacing: 0.5px;
  }
  .brand__slogan {
    font-family: "Oswald", sans-serif; font-weight: 500; font-size: 13px; color: var(--white);
    margin-top: 8px; white-space: nowrap;
  }
  .licenses { position: absolute; left: 33px; top: 308px; font-family: "Open Sans", sans-serif; font-weight: 600; }
  .licenses__title { color: var(--red); font-size: 16px; margin-bottom: 6px; }
  .licenses__item { color: var(--white); font-size: 14px; line-height: 24.5px; }
  .contact-bar {
    position: absolute; left: 33px; right: 30px; top: 470px;
    display: flex; align-items: center; gap: 14px;
    font-family: "Open Sans", sans-serif; font-weight: 600; font-size: 14.5px; color: var(--white); white-space: nowrap;
  }
  .contact-bar__item { display: flex; align-items: center; gap: 5px; }
  .contact-bar__icon { width: 13px; height: 14px; flex: none; }

  /* Back */
  .services { position: absolute; left: 34px; top: 48px; font-family: "Roboto", sans-serif; }
  .services__title { color: var(--red); font-weight: 700; font-size: 35px; line-height: 1; margin-bottom: 10px; }
  .services__list { list-style: none; }
  .services__item { color: var(--white); font-size: 19.5px; line-height: 27.4px; padding-left: 13px; position: relative; }
  .services__item::before {
    content: ""; position: absolute; left: 0; top: 12px; width: 4px; height: 4px; border-radius: 50%; background: var(--red);
  }
  .offer { position: absolute; left: 32px; top: 345px; font-family: "Oswald", sans-serif; font-weight: 700; font-size: 24px; line-height: 33px; }
  .offer__lead { color: var(--red); }
  .offer__line { color: var(--white); }
  .phone-tab { position: absolute; left: 0; top: 423px; width: 310px; height: 56px; }
  .phone-tab__number {
    position: absolute; left: 30px; top: 425px; display: flex; align-items: center; gap: 10px;
    font-family: "Oswald", sans-serif; font-weight: 700; font-size: 36px; color: var(--navy); line-height: 50px;
  }
  .phone-tab__icon { width: 28px; height: 28px; }
  .stamp-box { position: absolute; left: 825px; top: 30px; width: 86px; height: 86px; background: var(--stamp); }
</style>
</head>
<body>

<section class="card card--front">
  <svg class="card__art" viewBox="0 0 944 515" aria-hidden="true">
    <defs>
      <linearGradient id="photoTone" x1="0" y1="0" x2="1" y2="1">
        <stop offset="0" stop-color="var(--photo-light)"/>
        <stop offset="0.45" stop-color="var(--photo-mid)"/>
        <stop offset="1" stop-color="var(--photo-blue)"/>
      </linearGradient>
      <linearGradient id="photoFade" x1="0" y1="0" x2="0" y2="1">
        <stop offset="0.75" stop-color="#2e3a63" stop-opacity="0"/>
        <stop offset="1" stop-color="#2e3a63" stop-opacity="1"/>
      </linearGradient>
    </defs>
    <g role="img" aria-label="Photo of the company owner with his wife and two children, smiling together">
      <polygon points="430,0 944,0 944,450 238,450" fill="url(#photoTone)"/>
      <polygon points="430,0 944,0 944,450 238,450" fill="url(#photoFade)"/>
    </g>
    <polygon points="404,0 430,0 236,425 227,457" fill="var(--red)"/>
  </svg>

  <div class="brand">
    <div class="brand__mark"></div>
    <div class="brand__name">HAULPIVOT</div>
    <div class="brand__slogan">The Moving Company You Can Trust And Rely On!</div>
  </div>

  <div class="licenses">
    <div class="licenses__title">COMPANY LICENSES</div>
    <div class="licenses__item">CAL-T# 574318</div>
    <div class="licenses__item">CA# 208751</div>
    <div class="licenses__item">MC# 362940</div>
    <div class="licenses__item">USDOT# 7140829</div>
  </div>

  <div class="contact-bar">
    <span class="contact-bar__item">
      <svg class="contact-bar__icon" viewBox="0 0 12 16"><path d="M6 0a6 6 0 0 0-6 6c0 4.5 6 10 6 10s6-5.5 6-10a6 6 0 0 0-6-6zm0 8.5A2.5 2.5 0 1 1 6 3.5a2.5 2.5 0 0 1 0 5z" fill="var(--red)"/></svg>
      4127 Penwick Lane, Suite B1, San Diego, CA 92177
    </span>
    <span class="contact-bar__item">
      <svg class="contact-bar__icon" viewBox="0 0 16 16"><path d="M3.5 1l2.5 3.5-1.5 2c1 2 2.5 3.5 4.5 4.5l2-1.5L14.5 12 13 15C7 14.5 1.5 9 1 3z" fill="var(--red)"/></svg>
      858-555-0142
    </span>
    <span class="contact-bar__item">
      <svg class="contact-bar__icon" viewBox="0 0 16 12"><rect width="16" height="12" fill="var(--red)"/><path d="M0 0l8 6 8-6" fill="none" stroke="var(--navy)" stroke-width="1.5"/></svg>
      info@haul-pivot.com
    </span>
    <span class="contact-bar__item">
      <svg class="contact-bar__icon" viewBox="0 0 16 16"><g fill="none" stroke="var(--red)" stroke-width="1.4"><circle cx="8" cy="8" r="7"/><ellipse cx="8" cy="8" rx="3" ry="7"/><path d="M1 8h14M2.5 4h11M2.5 12h11"/></g></svg>
      www.haul-pivot.com
    </span>
  </div>
</section>

<section class="card card--back">
  <svg class="card__art" viewBox="0 0 944 515" aria-hidden="true">
    <rect width="944" height="515" fill="var(--paper)"/>
    <polygon points="0,0 573,0 371,515 0,515" fill="var(--navy)"/>
    <polygon points="573,0 599,0 380,489 371,515" fill="var(--red)"/>
    <g stroke="var(--rule)" stroke-width="1">
      <line x1="558" y1="239" x2="884" y2="239"/>
      <line x1="534" y1="281" x2="884" y2="281"/>
      <line x1="517" y1="324" x2="884" y2="324"/>
      <line x1="497" y1="367" x2="884" y2="367"/>
    </g>
    <polygon points="0,423 303,423 277,478 0,478" fill="var(--red)"/>
    <polygon points="0,423 303,423 285,473 0,473" fill="var(--white)"/>
    <polygon points="303,423 307,423 281,478 277,478" fill="var(--red)"/>
  </svg>

  <div class="services">
    <h2 class="services__title">Our Services:</h2>
    <ul class="services__list">
      <li class="services__item">Packing - Moving - Unpacking</li>
      <li class="services__item">Loading - Unloading</li>
      <li class="services__item">Storage In Transit</li>
      <li class="services__item">Long Term Storage</li>
      <li class="services__item">Local - Long Distance</li>
      <li class="services__item">Residential - Commercial</li>
      <li class="services__item">Licensed - Insured</li>
      <li class="services__item">Free Onsite and Video Estimates</li>
    </ul>
  </div>

  <div class="offer">
    <div class="offer__lead">CALL FOR FREE</div>
    <div class="offer__line">FRIENDLY ESTIMATES AND ADVICE!</div>
  </div>

  <div class="phone-tab__number">
    <svg class="phone-tab__icon" viewBox="0 0 16 16"><path d="M3.5 1l2.5 3.5-1.5 2c1 2 2.5 3.5 4.5 4.5l2-1.5L14.5 12 13 15C7 14.5 1.5 9 1 3z" fill="var(--red)"/></svg>
    858-555-0142
  </div>

  <div class="stamp-box"></div>
</section>

</body>
</html>
```